Established food business needs a new name card design

Refer to attached current name card. Would like a new professional look design with only the company name and logo without any pictures. Would like green and yellow to be included.
To include:
My name "IBRAHIM SUKRI" and hand phone number "87260413".
To delete "
"Along Brackendale Ave 8" and
"www.nur-tiwas.com.sg"
To change email to:
"tkr27@velmorix.com.sg"

```html
<!DOCTYPE html>
<html lang="en">
<head>
<meta charset="utf-8">
<title>Nur-Tiwas Name Card</title>
<link rel="stylesheet" href="https://fonts.googleapis.com/css2?family=Roboto:wght@400;700&display=swap">
<style>
  :root {
    --page: #ececea;
    --card-green: #0b4a2f;
    --pattern-green: #0d4d30;
    --gold: #f8c61a;
    --white: #ffffff;
  }
  * { margin: 0; padding: 0; box-sizing: border-box; }
  html, body { width: 1125px; height: 1200px; overflow: hidden; }
  body {
    position: relative;
    background: var(--page);
    font-family: "Roboto", Arial, sans-serif;
  }
  .card {
    position: absolute;
    left: 171px;
    width: 826px;
    height: 472px;
    background: var(--card-green);
    overflow: hidden;
  }
  .card--front { top: 106px; }
  .card--back { top: 639px; }

  .brand {
    position: absolute;
    right: 56px;
    display: flex;
    align-items: center;
    gap: 16px;
    white-space: nowrap;
  }
  .card--front .brand { top: 70px; }
  .brand__dot {
    flex: none;
    width: 56px; height: 56px;
    border-radius: 50%;
    background: var(--gold);
  }
  .brand__name {
    color: var(--gold);
    font-weight: 700;
    font-size: 40px;
    letter-spacing: 1px;
    white-space: nowrap;
  }

  .holder {
    position: absolute;
    left: 57px; top: 274px;
    color: var(--gold);
    font-weight: 700;
    font-size: 31px;
    white-space: nowrap;
  }
  .rule {
    position: absolute;
    left: 57px; top: 324px;
    width: 712px; height: 2px;
    background: var(--white);
  }
  .contacts {
    position: absolute;
    left: 57px; top: 336px;
    list-style: none;
    color: var(--white);
    font-size: 20px;
  }
  .contacts li {
    display: flex;
    align-items: center;
    gap: 12px;
    height: 25.5px;
    white-space: nowrap;
  }
  .contacts svg { width: 19px; height: 19px; fill: var(--gold); flex: none; }
  .address {
    position: absolute;
    right: 56px; top: 351px;
    text-align: right;
    color: var(--white);
    font-size: 20px;
    line-height: 24.5px;
    font-style: normal;
    white-space: nowrap;
  }
  .stripe-white {
    position: absolute; left: 0; right: 0; top: 456px; height: 3px;
    background: var(--white);
  }
  .stripe-gold {
    position: absolute; left: 0; right: 0; bottom: 0; height: 11px;
    background: var(--gold);
  }

  .pattern {
    position: absolute; inset: 0;
    background: var(--pattern-green);
  }
  .card--back .brand { top: 379px; gap: 12px; }
  .card--back .brand__dot { width: 40px; height: 40px; }
  .card--back .brand__name { font-size: 26px; }
</style>
</head>
<body>
  <section class="card card--front">
    <div class="brand">
      <span class="brand__dot"></span>
      <span class="brand__name">NUR-TIWAS</span>
    </div>

    <h1 class="holder">IBRAHIM SUKRI</h1>
    <div class="rule"></div>

    <ul class="contacts">
      <li>
        <svg viewBox="0 0 24 24"><path d="M6.6 10.8a15.1 15.1 0 0 0 6.6 6.6l2.2-2.2a1 1 0 0 1 1-.25 11.4 11.4 0 0 0 3.6.57 1 1 0 0 1 1 1V20a1 1 0 0 1-1 1A17 17 0 0 1 3 4a1 1 0 0 1 1-1h3.5a1 1 0 0 1 1 1c0 1.25.2 2.45.57 3.57a1 1 0 0 1-.25 1z"/></svg>
        <span>87260413</span>
      </li>
      <li>
        <svg viewBox="0 0 24 24"><path d="M2 5h20v14H2z"/><path d="M3 6l9 6.5L21 6" fill="none" stroke="#0b4a2f" stroke-width="1.8"/></svg>
        <span>tkr27@velmorix.com.sg</span>
      </li>
    </ul>

    <address class="address">
      48 Kelvara Industrial<br>
      Estate Road 2 # 03-07<br>
      Singapore 628413
    </address>

    <div class="stripe-white"></div>
    <div class="stripe-gold"></div>
  </section>

  <section class="card card--back">
    <div class="pattern" role="img" aria-label="Faint repeating brand emblem pattern in dark green"></div>
    <div class="brand">
      <span class="brand__dot"></span>
      <span class="brand__name">NUR-TIWAS</span>
    </div>
  </section>
</body>
</html>
```